we need a homepage for a marketplace

We manage all projects using our ground-breaking platform Kelvrim Hub. You get access to 150+ partners in 70 countries, security, cost efficiency, technical skills, speed, 100% visibility and accountability.Kelvrim aims to help clients realize the full potential of their investments, provide a competitive price, establish the business need as a competitive advantage, and provide a strategic business asset that can facilitate growth.
Target Market(s)
Freelancers
Industry/Entity Type
Business Software
Number of Pages Required
1 page
Requirements
Must have
- Credentials -http://qabdel.example/freelancer/public
- Front :
- Client:
- Email id - tomasp@lurvantsystems.example
- Password - 908172
- Partner:
- Email id - dorian@lurvantsystems.example
- Password - 908172
- Project Manager:
- Email id - mirela@lurvantsystems.example
- Password - 908172
Nice to have
- It will be nice to have a creative design, and a outside the box look/feel

```html
<!DOCTYPE html>
<html lang="en">
<head>
<meta charset="utf-8">
<title>Kelvrim – Marketplace</title>
<link href="https://fonts.googleapis.com/css2?family=Raleway:wght@400;600;700&family=Open+Sans:ital,wght@0,400;0,600;0,700;1,400&display=swap" rel="stylesheet">
<style>
:root{
  --blue:#3aa9d4;
  --blue-dark:#1f86b4;
  --orange:#f7941d;
  --ink:#333333;
  --muted:#6b6b6b;
  --light:#f2f2f2;
  --footer:#3b3b3b;
  --line:#dcdcdc;
  --white:#ffffff;
}
*{box-sizing:border-box;margin:0;padding:0}
html,body{width:1200px;height:3203px;overflow:hidden}
body{font-family:"Open Sans",Arial,sans-serif;color:var(--ink);background:var(--white);position:relative}
.section{position:absolute;left:0;width:1200px;overflow:hidden}
.btn{position:absolute;display:flex;align-items:center;justify-content:center;font-family:"Raleway",Arial,sans-serif;font-weight:700;font-size:12px;color:var(--white);text-transform:uppercase;letter-spacing:.3px}
.btn-orange{background:var(--orange)}
.btn-blue{background:var(--blue)}

/* hero */
.hero{top:0;height:566px}
.hero-bg{position:absolute;inset:0;background:linear-gradient(115deg,#2a2522 0%,#3b3430 40%,#1e1c1c 70%,#2d2926 100%)}
.brand{position:absolute;left:160px;top:48px;display:flex;align-items:center;gap:10px;font-family:"Raleway",Arial,sans-serif;font-weight:600;font-size:34px;color:var(--white)}
.brand-dot{width:16px;height:16px;border-radius:50%;background:var(--blue)}
.nav{position:absolute;top:54px;left:474px;font-family:"Raleway",Arial,sans-serif;font-size:12px;font-weight:600;color:var(--white);text-transform:uppercase}
.nav a{position:absolute;white-space:nowrap;color:var(--white);text-decoration:none}
.nav a.active{color:var(--blue)}
.hero-title{position:absolute;left:160px;top:226px;width:440px;font-family:"Raleway",Arial,sans-serif;font-weight:700;font-size:30px;line-height:40px;color:var(--white)}
.hero-text{position:absolute;left:160px;top:324px;width:440px;font-size:13px;line-height:20px;color:#e6e6e6}
.hero-btn{left:160px;top:386px;width:192px;height:43px;gap:8px}
.hero-btn .ic{width:18px;height:18px;border-radius:50%;background:var(--white)}
.dots{position:absolute;left:162px;top:510px;display:flex;gap:8px}
.dots span{width:28px;height:4px;background:var(--white)}
.dots span.on{background:var(--blue)}
.laptop-screen{position:absolute;left:614px;top:263px;width:422px;height:285px;border:10px solid #111;border-radius:10px 10px 0 0;background:linear-gradient(160deg,#2a86b8 0%,#7fc4e4 35%,#eef3f6 36%,#f5f5f5 100%)}
.laptop-base{position:absolute;left:588px;top:548px;width:474px;height:12px;background:linear-gradient(#d9d9d9,#9a9a9a);border-radius:0 0 14px 14px}

/* how it works */
.how{top:566px;height:380px}
.sec-title{position:absolute;left:0;width:1200px;text-align:center;font-family:"Raleway",Arial,sans-serif;font-weight:600;font-size:17px;letter-spacing:1px;text-transform:uppercase;color:#444}
.sec-lead{position:absolute;left:320px;width:560px;text-align:center;font-size:11px;line-height:17px;color:var(--muted)}
.step{position:absolute;top:112px;width:200px;text-align:center}
.step-ring{display:block;margin:0 auto;width:140px;height:140px}
.step h3{margin-top:12px;font-family:"Raleway",Arial,sans-serif;font-size:13px;font-weight:600;color:#333}
.step p{margin-top:10px;font-size:11px;line-height:17px;color:var(--muted)}
.connector{position:absolute;top:128px}

/* features */
.features{top:946px;height:356px;background:linear-gradient(90deg,#2d8fbf 0%,#3aa9d4 45%,#3aa9d4 100%)}
.devices-art{position:absolute;left:160px;top:57px;width:460px;height:257px;border-radius:6px;background:linear-gradient(135deg,rgba(255,255,255,.25),rgba(255,255,255,.08))}
.feat-title{position:absolute;left:662px;top:40px;font-family:"Raleway",Arial,sans-serif;font-weight:700;font-size:22px;color:var(--white);letter-spacing:.5px}
.feat-lead{position:absolute;left:662px;top:78px;width:400px;font-size:12px;line-height:18px;color:#e3f3fa}
.feat-list{position:absolute;left:662px;top:138px;list-style:none}
.feat-list li{display:flex;align-items:center;gap:10px;height:29px;font-size:11px;color:var(--white);white-space:nowrap}
.feat-list .tick{flex:none;width:14px;height:14px;border-radius:50%;background:var(--white);display:flex;align-items:center;justify-content:center}
.store{position:absolute;top:271px;height:43px;border:2px solid #ccc;border-radius:7px;background:#111;display:flex;align-items:center;padding-left:12px}
.store span{display:block;width:22px;height:22px;border-radius:4px;background:#777}

/* talent */
.talent{top:1302px;height:374px}
.col-title{position:absolute;top:50px;font-family:"Raleway",Arial,sans-serif;font-weight:600;font-size:18px;color:#333}
.talent-copy{position:absolute;left:160px;top:92px;width:424px}
.talent-copy p{font-size:11px;line-height:18px;color:var(--muted);margin-bottom:12px}
.talent-copy .btn{position:static;display:inline-flex;width:102px;height:34px;margin-top:2px}
.video{position:absolute;left:626px;top:94px;width:412px;height:229px;background:linear-gradient(120deg,#5f6f7d 0%,#2e3a46 45%,#c9cfd4 100%)}
.play{position:absolute;left:176px;top:84px;width:62px;height:62px;border:3px solid var(--white);border-radius:50%}

/* portal */
.portal{top:1676px;height:305px;background:var(--light)}
.portal-art{position:absolute;left:139px;top:64px;width:437px;height:160px;border-radius:4px;background:linear-gradient(180deg,#1e6f9a 0%,#4aa7d1 55%,#d9d9d9 56%,#bfbfbf 100%)}
.portal h2{position:absolute;left:606px;top:74px;width:440px;font-family:"Raleway",Arial,sans-serif;font-weight:700;font-size:18px;line-height:24px;color:#444}
.portal p{position:absolute;left:606px;top:134px;width:440px;font-size:11px;line-height:18px;color:var(--muted)}

/* testimonials */
.testi{top:1981px;height:361px}
.testi-bg{position:absolute;inset:0;background:linear-gradient(100deg,#4a4440 0%,#5c5550 40%,#3e3a37 100%)}
.testi h2{top:70px;color:var(--white)}
.arrows{position:absolute;left:985px;top:70px;display:flex;gap:6px}
.arrows span{width:24px;height:24px;border:2px solid #ddd;border-radius:50%}
.avatar{position:absolute;left:190px;top:136px;width:126px;height:126px;border-radius:50%;border:5px solid var(--white);background:linear-gradient(160deg,#c9a88a,#e8ddd2)}
.quote{position:absolute;left:342px;top:134px;width:680px;font-style:italic;font-size:13px;line-height:25px;color:#eeeeee}
.quote b{font-style:normal;font-size:24px;font-weight:700;color:var(--white);vertical-align:-4px;line-height:0}
.author{position:absolute;left:342px;top:230px;font-family:"Raleway",Arial,sans-serif;font-weight:700;font-size:12px;color:var(--white);text-transform:uppercase}
.author small{font-weight:600;color:#bbb;font-size:10px}

/* benefits */
.benefits{top:2342px;height:536px}
.benefit{position:absolute;width:290px;height:90px}
.benefit .bi{position:absolute;left:0;top:0;width:56px;height:56px;border-radius:50%;display:flex;align-items:center;justify-content:center}
.bi.solid{background:var(--blue)}
.bi.ring{border:2px solid var(--blue)}
.benefit h3{position:absolute;left:74px;top:-6px;font-family:"Raleway",Arial,sans-serif;font-size:15px;font-weight:600;color:var(--orange)}
.benefit p{position:absolute;left:74px;top:20px;width:200px;font-size:10.5px;line-height:17px;color:var(--muted)}
.badges{position:absolute;left:180px;top:378px;display:grid;grid-template-columns:repeat(8,88px);column-gap:16px;row-gap:20px}
.badges span{height:28px;background:#bdbdbd;border-radius:3px}
.badges span:nth-child(3n){border-radius:14px;background:#c8c8c8}
.badges span:nth-child(4n){background:#a9a9a9}

/* footer */
.footer{top:2878px;height:239px;background:var(--footer);color:#cfcfcf}
.f-brand{position:absolute;left:160px;top:48px;font-family:"Raleway",Arial,sans-serif;font-weight:600;font-size:24px;color:var(--white)}
.f-about{position:absolute;left:160px;top:116px;width:125px;font-size:10.5px;line-height:19px;color:#d8d8d8}
.f-divider{position:absolute;left:295px;top:0;width:1px;height:239px;background:#555}
.f-col{position:absolute;top:44px;width:200px}
.f-col h4{font-family:"Raleway",Arial,sans-serif;font-weight:700;font-size:14px;color:var(--white);margin-bottom:10px;text-transform:uppercase}
.f-col ul{list-style:none;font-size:11.5px;line-height:21px;color:#e0e0e0}
.f-item{margin-bottom:14px;font-size:11px;line-height:17px}
.f-item strong{display:block;font-weight:400;color:#e6e6e6;font-size:12px}
.f-item span{color:#b9b9b9}
.f-item em{font-style:normal;color:var(--orange)}
.f-input{width:190px;height:34px;background:var(--white);font-size:10px;color:#999;padding:0 10px;display:flex;align-items:center;margin-top:12px}
.f-sub{position:relative;margin-top:10px;width:92px;height:30px}

/* bottom bar */
.bar{top:3117px;height:86px;background:var(--blue);color:var(--white)}
.bar-legal{position:absolute;left:160px;top:26px;font-size:10.5px;line-height:21px}
.bar-name{position:absolute;left:798px;top:30px;font-family:"Raleway",Arial,sans-serif;font-size:18px;font-weight:600}
.social{position:absolute;left:910px;top:26px;display:flex;gap:6px}
.social span{width:30px;height:30px;border-radius:50%;background:var(--white);border:3px solid #2f8fba}
</style>
</head>
<body>

<header class="section hero">
  <div class="hero-bg" role="img" aria-label="Dark photo of hands working at a laptop on a desk"></div>
  <div class="brand"><span class="brand-dot"></span>Kelvrim</div>
  <nav class="nav">
    <a class="active" style="left:0">Home</a>
    <a style="left:77px">How it works</a>
    <a style="left:211px">About</a>
    <a style="left:295px">Contact</a>
    <a style="left:393px">Team</a>
  </nav>
  <div class="btn btn-orange" style="left:935px;top:47px;width:103px;height:32px;font-size:10px">Add Project</div>
  <h1 class="hero-title">Mobile &amp; web applications using latest technologies.</h1>
  <p class="hero-text">Sed ut perspiciatis unde omnis iste natuseor sit voluptate m accusantiumdol orem qulaudantium.</p>
  <div class="btn btn-blue hero-btn"><span class="ic"></span>Post your project</div>
  <div class="dots"><span></span><span></span><span class="on"></span><span></span></div>
  <div class="laptop-screen" role="img" aria-label="Laptop showing the project details dashboard"></div>
  <div class="laptop-base"></div>
</header>

<section class="section how">
  <h2 class="sec-title" style="top:42px">How it works</h2>
  <p class="sec-lead" style="top:72px">Sed ut perspiciatis unde omnis iste natus error sit voluptatem accusantium doloremque laudantium, totam rem aperiam, eaque ipsa quae ab illo inventore veritatis et quasi architecto beatae vitae dict a sunt explicabo.</p>

  <svg class="connector" style="left:314px" width="110" height="60" viewBox="0 0 110 60"><path d="M5 20 Q55 -6 100 40" fill="none" stroke="#cfcfcf" stroke-width="2" stroke-dasharray="4 4"/><path d="M92 36 L102 42 L98 30" fill="none" stroke="#cfcfcf" stroke-width="2"/></svg>
  <svg class="connector" style="left:556px" width="110" height="60" viewBox="0 0 110 60"><path d="M5 40 Q55 66 100 20" fill="none" stroke="#cfcfcf" stroke-width="2" stroke-dasharray="4 4"/><path d="M92 18 L102 18 L98 30" fill="none" stroke="#cfcfcf" stroke-width="2"/></svg>
  <svg class="connector" style="left:788px" width="110" height="60" viewBox="0 0 110 60"><path d="M5 20 Q55 -6 100 40" fill="none" stroke="#cfcfcf" stroke-width="2" stroke-dasharray="4 4"/><path d="M92 36 L102 42 L98 30" fill="none" stroke="#cfcfcf" stroke-width="2"/></svg>

  <div class="step" style="left:146px">
    <svg class="step-ring" viewBox="0 0 140 140"><circle cx="70" cy="70" r="64" fill="#fff" stroke="#e3e3e3" stroke-width="8"/><path d="M70 6 A64 64 0 0 1 134 70" fill="none" stroke="#f7941d" stroke-width="8"/><circle cx="70" cy="70" r="48" fill="#3aa9d4"/><rect x="52" y="57" width="36" height="24" rx="2" fill="none" stroke="#fff" stroke-width="3"/><path d="M64 87h12" stroke="#fff" stroke-width="3"/></svg>
    <h3>Post Your Project</h3>
    <p>Sed ut perspiciatis unde omnisnat serror sit voluptatem accusantiudol oremque laudantium, totam re.</p>
  </div>
  <div class="step" style="left:391px">
    <svg class="step-ring" viewBox="0 0 140 140"><circle cx="70" cy="70" r="64" fill="#fff" stroke="#e3e3e3" stroke-width="8"/><path d="M70 6 A64 64 0 0 1 125 38" fill="none" stroke="#f7941d" stroke-width="8"/><circle cx="70" cy="70" r="48" fill="#3aa9d4"/><path d="M54 70 l11 11 l22 -24" fill="none" stroke="#fff" stroke-width="5" stroke-linecap="round"/></svg>
    <h3>Select an Expert</h3>
    <p>Sed ut perspiciatis unde omnisnat serror sit voluptatem accusantiudol oremque laudantium, totam re.</p>
  </div>
  <div class="step" style="left:620px">
    <svg class="step-ring" viewBox="0 0 140 140"><circle cx="70" cy="70" r="64" fill="#fff" stroke="#e3e3e3" stroke-width="8"/><path d="M6 70 A64 64 0 0 1 70 6" fill="none" stroke="#f7941d" stroke-width="8"/><circle cx="70" cy="70" r="48" fill="#3aa9d4"/><circle cx="70" cy="70" r="12" fill="none" stroke="#fff" stroke-width="6"/><g stroke="#fff" stroke-width="6" stroke-linecap="round"><path d="M70 50v-4M70 94v-4M50 70h-4M94 70h-4M56 56l-3-3M84 84l3 3M56 84l-3 3M84 56l3-3"/></g></svg>
    <h3>Work on the Project</h3>
    <p>Sed ut perspiciatis unde omnisnat serror sit voluptatem accusantiudol oremque laudantium, totam re.</p>
  </div>
  <div class="step" style="left:865px">
    <svg class="step-ring" viewBox="0 0 140 140"><circle cx="70" cy="70" r="64" fill="#fff" stroke="#e3e3e3" stroke-width="8"/><path d="M70 134 A64 64 0 0 1 6 70" fill="none" stroke="#f7941d" stroke-width="8"/><circle cx="70" cy="70" r="48" fill="#3aa9d4"/><rect x="48" y="56" width="44" height="28" rx="2" fill="none" stroke="#fff" stroke-width="3"/><circle cx="70" cy="70" r="7" fill="none" stroke="#fff" stroke-width="3"/></svg>
    <h3>Pay only when Satisfied</h3>
    <p>Sed ut perspiciatis unde omnisnat serror sit voluptatem accusantiudol oremque laudantium, totam re.</p>
  </div>
</section>

<section class="section features">
  <div class="devices-art" role="img" aria-label="Desktop, laptop, tablet and phone showing the platform"></div>
  <h2 class="feat-title">OUR FEATURES</h2>
  <p class="feat-lead">At vero eos et accusamus et iusto odio dignissimos ducimus qui entium voluptatum del eniti atque corrupti quos.</p>
  <ul class="feat-list">
    <li><span class="tick"><svg width="9" height="9" viewBox="0 0 10 10"><path d="M2 5l2 2 4-5" fill="none" stroke="#3aa9d4" stroke-width="2"/></svg></span>On the other hand, we denounce with righteous indignation and dislike.</li>
    <li><span class="tick"><svg width="9" height="9" viewBox="0 0 10 10"><path d="M2 5l2 2 4-5" fill="none" stroke="#3aa9d4" stroke-width="2"/></svg></span>At vero eos et accusamus et iusto odio dignissimos ducimus qui blanditiis.</li>
    <li><span class="tick"><svg width="9" height="9" viewBox="0 0 10 10"><path d="M2 5l2 2 4-5" fill="none" stroke="#3aa9d4" stroke-width="2"/></svg></span>Certain circumstances and owing to the claims of duty or the oblig</li>
    <li><span class="tick"><svg width="9" height="9" viewBox="0 0 10 10"><path d="M2 5l2 2 4-5" fill="none" stroke="#3aa9d4" stroke-width="2"/></svg></span>On the other hand, we denounce with righteous indignation and dislike.</li>
  </ul>
  <div class="store" style="left:662px;width:132px"><span></span></div>
  <div class="store" style="left:811px;width:137px"><span></span></div>
</section>

<section class="section talent">
  <h2 class="col-title" style="left:160px">Top Talent at your Disposal</h2>
  <div class="talent-copy">
    <p>Sed ut perspiciatis unde omnis iste natus error sit voluptatem accusantium dolorem que laudantium, totam rem aperiam, eaque ipsa quae ab illo inventore veritatis et qu asi architecto beatae vitae dicta sunt explicabo. Nemo enim ipsam voluptatem quia vo luptas sit aspernatur aut odit aut fugit, sed quia consequuntur magni dolores eos qui ratione voluptatem sequi nesciuntque porro quisquam est, qui dolorem ipsum.</p>
    <p>Sptas sit aspernatur aut odit aut fugit, sed quia consequuntur magni dolores eos qui ratione voluptatem sequi nesciunt. Neque porro quisquam est, qui dolorem ipsum qu ia dolor sit amet, consectetur, adipisci velit, sed quia non numquam eius modi tempo ra incidunt ut labore et dolore magnam aliquam.</p>
    <div class="btn btn-orange">Read more</div>
  </div>
  <h2 class="col-title" style="left:626px">Who Are We</h2>
  <div class="video" role="img" aria-label="Video still of a developer coding at a monitor"><span class="play"></span></div>
</section>

<section class="section portal">
  <div class="portal-art" role="img" aria-label="Laptops and monitors showing the Kelvrim Hub login screen"></div>
  <h2>We manage all projects using our<br>ground-breaking platform Kelvrim Hub</h2>
  <p>Sed ut perspiciatis unde omnis iste natus error sit voluptatem accusantium doloremque laudantium, totam rem aperiam, eaque ipsa quae ab illo inventore veritatis et quasi arc hitecto beate vitae dict a sunt explicabod ut perspiciatis unde omni</p>
  <div class="btn btn-orange" style="left:606px;top:207px;width:167px;height:34px">Become a partner</div>
</section>

<section class="section testi">
  <div class="testi-bg" role="img" aria-label="Blurred photo of a team meeting"></div>
  <h2 class="sec-title">Testimonials</h2>
  <div class="arrows"><span></span><span></span></div>
  <div class="avatar" role="img" aria-label="Client portrait"></div>
  <p class="quote"><b>“</b> Sed ut perspiciatis unde omnis iste natus error sit voluptatem accusantium doloremque laudantium, totam rem aperiam, eaque ipsa quae ab illo inventore veritatis et quasi architecto beatae vitae dicta sunt explicaboni mpsam voluptatem quia voluptas sit aspernatur aut odit aut fugit, sed quia consequuntur magni <b>”</b></p>
  <div class="author">Rafe Dunmore, <small>City name, Lorem sipmdil</small></div>
</section>

<section class="section benefits">
  <h2 class="sec-title" style="top:44px">You get access to 150+ partners in 70 countries</h2>

  <div class="benefit" style="left:160px;top:112px"><div class="bi solid"><svg width="24" height="24" viewBox="0 0 24 24"><path d="M3 10v4h4l8 5V5L7 10z" fill="#fff"/></svg></div><h3>Security</h3><p>Sed ut perspiciatis unde omnis iste nater ror sit voluptatem accusantium dolorque laudantium, totam rem aperiam.</p></div>
  <div class="benefit" style="left:465px;top:112px"><div class="bi ring"><svg width="22" height="22" viewBox="0 0 24 24"><rect x="4" y="5" width="16" height="15" rx="1" fill="none" stroke="#3aa9d4" stroke-width="2"/><path d="M4 10h16" stroke="#3aa9d4" stroke-width="2"/></svg></div><h3>Cost Efficiency</h3><p>Sed ut perspiciatis unde omnis iste nater ror sit voluptatem accusantium dolorque laudantium, totam rem aperiam.</p></div>
  <div class="benefit" style="left:770px;top:112px"><div class="bi ring"><svg width="22" height="22" viewBox="0 0 24 24"><path d="M3 12l18-8-6 17-3-7z" fill="#3aa9d4"/></svg></div><h3>Technical Skills</h3><p>Sed ut perspiciatis unde omnis iste nater ror sit voluptatem accusantium dolorque laudantium, totam rem aperiam.</p></div>
  <div class="benefit" style="left:160px;top:232px"><div class="bi ring"><svg width="22" height="22" viewBox="0 0 24 24"><circle cx="7" cy="12" r="3" fill="#3aa9d4"/><circle cx="17" cy="6" r="3" fill="#3aa9d4"/><circle cx="17" cy="18" r="3" fill="#3aa9d4"/><path d="M7 12L17 6M7 12l10 6" stroke="#3aa9d4" stroke-width="2"/></svg></div><h3>Speed</h3><p>Sed ut perspiciatis unde omnis iste nater ror sit voluptatem accusantium dolorque laudantium, totam rem aperiam.</p></div>
  <div class="benefit" style="left:465px;top:232px"><div class="bi ring"><svg width="22" height="22" viewBox="0 0 24 24"><path d="M5 12l5 5 9-10" fill="none" stroke="#3aa9d4" stroke-width="3"/></svg></div><h3>100% Visibility</h3><p>Sed ut perspiciatis unde omnis iste nater ror sit voluptatem accusantium dolorque laudantium, totam rem aperiam.</p></div>
  <div class="benefit" style="left:770px;top:232px"><div class="bi ring"><svg width="22" height="22" viewBox="0 0 24 24"><rect x="5" y="10" width="14" height="11" rx="1" fill="#3aa9d4"/><path d="M8 10V7a4 4 0 018 0v3" fill="none" stroke="#3aa9d4" stroke-width="2"/></svg></div><h3>Accountability</h3><p>Sed ut perspiciatis unde omnis iste nater ror sit voluptatem accusantium dolorque laudantium, totam rem aperiam.</p></div>

  <div class="badges" aria-label="Partner badges">
    <span></span><span></span><span></span><span></span><span></span><span></span><span></span><span></span>
    <span></span><span></span><span></span><span></span><span></span><span></span><span></span><span></span>
  </div>
</section>

<footer class="section footer">
  <div class="f-brand">Kelvrim</div>
  <p class="f-about">Duis aute irure dolor in reprehenderit in volupt ate velit esse cillum...</p>
  <div class="f-divider"></div>
  <div class="f-col" style="left:320px;width:90px"><h4>Career</h4><ul><li>API</li><li>Mobile Apps</li><li>Downloads</li><li>Tutorials</li><li>FAQ</li></ul></div>
  <div class="f-col" style="left:423px"><h4>Event</h4>
    <div class="f-item"><strong>Nemo enim ipsam voluptatem</strong><span>Tempora incidunt ut labore et<br>magnam aliquam..</span><em>23 July, 2016</em></div>
    <div class="f-item"><strong>Nemo enim ipsam voluptatem</strong><span>Tempora incidunt ut labore et<br>magnam aliquam..</span><em>23 July, 2016</em></div>
  </div>
  <div class="f-col" style="left:634px"><h4>Blog</h4>
    <div class="f-item"><strong>Nemo enim ipsam voluptatem</strong><span>Tempora incidunt ut labore et<br>magnam aliquam..</span><em>23 July, 2016</em></div>
    <div class="f-item"><strong>Nemo enim ipsam voluptatem</strong><span>Tempora incidunt ut labore et<br>magnam aliquam..</span><em>23 July, 2016</em></div>
  </div>
  <div class="f-col" style="left:848px"><h4>Newsletter</h4>
    <div class="f-item" style="margin:0"><span>Tempora incidunt ut labore et<br>magnam aliquam..</span></div>
    <div class="f-input">E-Mail Address</div>
    <div class="btn btn-orange f-sub">Subscribe</div>
  </div>
</footer>

<section class="section bar">
  <p class="bar-legal">© 2016 Kelvrim.. All Copyrights are Reserved.<br>Privacy | Terms &amp; Conditions</p>
  <div class="bar-name">Kelvrim.</div>
  <div class="social" aria-label="Social links"><span></span><span></span><span></span><span></span></div>
</section>

</body>
</html>
```